Creation of design for a line of dietary supplements - 18 products

18 packages must be made in the same style, maintaining (maybe a slight change) the color scheme. All texts and their position, font and size must be preserved. The main graphic element is the nanoliposomal shell. In any form - voluminous, flat, but it must be conveyed in every design. The logo and flower must remain the same size.

Дизайн выглядит одинаково

Дизайн выглядит одинаково

Дизайн выглядит одинаково

```html
<!DOCTYPE html>
<html lang="en">
<head>
<meta charset="utf-8">
<title>Liposomal Supplement Line – Packaging Fronts</title>
<link href="https://fonts.googleapis.com/css2?family=Cabin:wght@500;600;700&display=swap" rel="stylesheet">
<style>
  :root {
    --canvas-bg: #e8e8ea;
    --box-bg: #ffffff;
    --footer-bar: #ececec;
    --ink-dark: #1b1b1b;
    --ink-muted: #555555;
    --title-light: #ffffff;
  }
  * { margin: 0; padding: 0; box-sizing: border-box; }
  html, body { width: 960px; height: 1200px; overflow: hidden; background: var(--canvas-bg); }
  .product-line {
    width: 960px; height: 1200px;
    display: grid;
    grid-template-columns: repeat(3, 204px);
    grid-template-rows: repeat(6, 140px);
    column-gap: 26px; row-gap: 36px;
    justify-content: center; align-content: center;
    font-family: "Cabin", sans-serif;
  }
  .pack {
    position: relative; overflow: hidden;
    background: var(--box-bg);
    width: 204px; height: 140px;
    box-shadow: 0 2px 6px rgba(0,0,0,.08);
  }
  .pack__band {
    position: absolute; left: 0; top: 0; width: 100%; height: 58px;
    background: var(--top);
  }
  .pack__strip {
    position: absolute; left: 8px; top: 56px; width: 200px; height: 25px;
    background: var(--strip);
    border-radius: 13px 0 0 13px;
  }
  .pack__title {
    position: absolute; left: 5px; top: 35px;
    font-size: 15.5px; font-weight: 700; letter-spacing: -.1px;
    color: var(--title-light); white-space: nowrap;
  }
  .pack--light .pack__title { color: var(--ink-dark); }
  .pack__subtitle {
    position: absolute; left: 17px; top: 59px;
    font-size: 6.2px; font-weight: 600; letter-spacing: .2px;
    color: var(--ink-dark); text-transform: uppercase; white-space: nowrap;
  }
  .pack__process {
    position: absolute; left: 22px; top: 69px;
    font-size: 3.6px; font-weight: 500; letter-spacing: .2px;
    color: var(--ink-muted); text-transform: uppercase; white-space: nowrap;
  }
  .pack__shell {
    position: absolute; left: 162px; top: 29px; width: 70px; height: 70px;
    border-radius: 50%;
    background: radial-gradient(circle, #ffffff 0 38%, var(--strip) 40% 55%, var(--top) 58% 100%);
  }
  .pack__note {
    position: absolute; left: 8px; top: 121px;
    font-size: 3.4px; font-weight: 500; color: var(--ink-muted);
    text-transform: uppercase; letter-spacing: .2px;
  }
  .pack__footer {
    position: absolute; left: 4px; right: 10px; top: 127px; height: 8px;
    background: var(--footer-bar);
    display: flex; justify-content: space-between; align-items: center;
    padding: 0 6px 0 5px;
    font-size: 4.4px; font-weight: 600; color: var(--ink-muted);
    text-transform: uppercase; letter-spacing: .2px;
  }
</style>
</head>
<body>
<main class="product-line">

  <article class="pack" style="--top:#12836d;--strip:#dfee9a">
    <div class="pack__band"></div><div class="pack__strip"></div>
    <div class="pack__shell" role="img" aria-label="Liposomal shell ring graphic"></div>
    <h2 class="pack__title">E214 HORMAVEN</h2>
    <p class="pack__subtitle">Hormonal balancer</p>
    <p class="pack__process">Processed with liposomal nanotechnology</p>
    <p class="pack__note">Dietary supplement product</p>
    <div class="pack__footer"><span>Genuine product of Thailand</span><span>30 capsules</span></div>
  </article>

  <article class="pack pack--light" style="--top:#c5e12a;--strip:#f3f28a">
    <div class="pack__band"></div><div class="pack__strip"></div>
    <div class="pack__shell" role="img" aria-label="Liposomal shell ring graphic"></div>
    <h2 class="pack__title">R512 CARBOSTOP</h2>
    <p class="pack__subtitle">Carbs blocking complex</p>
    <p class="pack__process">Processed with liposomal nanotechnology</p>
    <p class="pack__note">Dietary supplement product</p>
    <div class="pack__footer"><span>Genuine product of Thailand</span><span>30 capsules</span></div>
  </article>

  <article class="pack pack--light" style="--top:#fcd21a;--strip:#dbe7a6">
    <div class="pack__band"></div><div class="pack__strip"></div>
    <div class="pack__shell" role="img" aria-label="Liposomal shell ring graphic"></div>
    <h2 class="pack__title">E630 LIPOLEAN</h2>
    <p class="pack__subtitle">Lipids supressing complex</p>
    <p class="pack__process">Processed with liposomal nanotechnology</p>
    <p class="pack__note">Dietary supplement product</p>
    <div class="pack__footer"><span>Genuine product of Thailand</span><span>30 capsules</span></div>
  </article>

  <article class="pack" style="--top:#b0102f;--strip:#cfe6f5">
    <div class="pack__band"></div><div class="pack__strip"></div>
    <div class="pack__shell" role="img" aria-label="Liposomal shell ring graphic"></div>
    <h2 class="pack__title">I472 VENOTRIM</h2>
    <p class="pack__subtitle">Anti-varicosis complex</p>
    <p class="pack__process">Processed with liposomal nanotechnology</p>
    <p class="pack__note">Dietary supplement product</p>
    <div class="pack__footer"><span>Genuine product of Thailand</span><span>30 capsules</span></div>
  </article>

  <article class="pack" style="--top:#6b5db5;--strip:#cdeaea">
    <div class="pack__band"></div><div class="pack__strip"></div>
    <div class="pack__shell" role="img" aria-label="Liposomal shell ring graphic"></div>
    <h2 class="pack__title">G318 SERENIX</h2>
    <p class="pack__subtitle">Mood and sleep complex</p>
    <p class="pack__process">Processed with liposomal nanotechnology</p>
    <p class="pack__note">Dietary supplement product</p>
    <div class="pack__footer"><span>Genuine product of Thailand</span><span>30 capsules</span></div>
  </article>

  <article class="pack" style="--top:#7a3b26;--strip:#f7dea6">
    <div class="pack__band"></div><div class="pack__strip"></div>
    <div class="pack__shell" role="img" aria-label="Liposomal shell ring graphic"></div>
    <h2 class="pack__title">K205 HEPALUX</h2>
    <p class="pack__subtitle">Liver cleansing complex</p>
    <p class="pack__process">Processed with liposomal nanotechnology</p>
    <p class="pack__note">Dietary supplement product</p>
    <div class="pack__footer"><span>Genuine product of Thailand</span><span>30 capsules</span></div>
  </article>

  <article class="pack" style="--top:#8e1a7b;--strip:#faeaa0">
    <div class="pack__band"></div><div class="pack__strip"></div>
    <div class="pack__shell" role="img" aria-label="Liposomal shell ring graphic"></div>
    <h2 class="pack__title">L441 CAPILLEX</h2>
    <p class="pack__subtitle">Hair rejuvenating complex</p>
    <p class="pack__process">Processed with liposomal nanotechnology</p>
    <p class="pack__note">Dietary supplement product</p>
    <div class="pack__footer"><span>Genuine product of Thailand</span><span>30 capsules</span></div>
  </article>

  <article class="pack" style="--top:#d1143a;--strip:#f8f23a">
    <div class="pack__band"></div><div class="pack__strip"></div>
    <div class="pack__shell" role="img" aria-label="Liposomal shell ring graphic"></div>
    <h2 class="pack__title">L716 CLEARDERMA</h2>
    <p class="pack__subtitle">Anti-acne complex</p>
    <p class="pack__process">Processed with liposomal nanotechnology</p>
    <p class="pack__note">Dietary supplement product</p>
    <div class="pack__footer"><span>Genuine product of Thailand</span><span>30 capsules</span></div>
  </article>

  <article class="pack" style="--top:#9b137d;--strip:#f4c9d0">
    <div class="pack__band"></div><div class="pack__strip"></div>
    <div class="pack__shell" role="img" aria-label="Liposomal shell ring graphic"></div>
    <h2 class="pack__title">L287 DERMAQUIL</h2>
    <p class="pack__subtitle">Anti-eczema complex</p>
    <p class="pack__process">Processed with liposomal nanotechnology</p>
    <p class="pack__note">Dietary supplement product</p>
    <div class="pack__footer"><span>Genuine product of Thailand</span><span>30 capsules</span></div>
  </article>

  <article class="pack" style="--top:#0e3f91;--strip:#cfe6f6">
    <div class="pack__band"></div><div class="pack__strip"></div>
    <div class="pack__shell" role="img" aria-label="Liposomal shell ring graphic"></div>
    <h2 class="pack__title">L874 HYDROVEL</h2>
    <p class="pack__subtitle">Skin hydration enhancer</p>
    <p class="pack__process">Processed with liposomal nanotechnology</p>
    <p class="pack__note">Dietary supplement product</p>
    <div class="pack__footer"><span>Genuine product of Thailand</span><span>30 capsules</span></div>
  </article>

  <article class="pack" style="--top:#1565b0;--strip:#d9eaa6">
    <div class="pack__band"></div><div class="pack__strip"></div>
    <div class="pack__shell" role="img" aria-label="Liposomal shell ring graphic"></div>
    <h2 class="pack__title">L932 FIRMADERM</h2>
    <p class="pack__subtitle">Skin firming complex</p>
    <p class="pack__process">Processed with liposomal nanotechnology</p>
    <p class="pack__note">Dietary supplement product</p>
    <div class="pack__footer"><span>Genuine product of Thailand</span><span>30 capsules</span></div>
  </article>

  <article class="pack" style="--top:#6f5fb7;--strip:#f1f191">
    <div class="pack__band"></div><div class="pack__strip"></div>
    <div class="pack__shell" role="img" aria-label="Liposomal shell ring graphic"></div>
    <h2 class="pack__title">L806 LUMIVEX</h2>
    <p class="pack__subtitle">Anti-pigmentation complex</p>
    <p class="pack__process">Processed with liposomal nanotechnology</p>
    <p class="pack__note">Dietary supplement product</p>
    <div class="pack__footer"><span>Genuine product of Thailand</span><span>30 capsules</span></div>
  </article>

  <article class="pack" style="--top:#8a1d84;--strip:#f7d3b4">
    <div class="pack__band"></div><div class="pack__strip"></div>
    <div class="pack__shell" role="img" aria-label="Liposomal shell ring graphic"></div>
    <h2 class="pack__title">M362 COLLAVITA</h2>
    <p class="pack__subtitle">Collagen complex</p>
    <p class="pack__process">Processed with liposomal nanotechnology</p>
    <p class="pack__note">Dietary supplement product</p>
    <div class="pack__footer"><span>Genuine product of Thailand</span><span>30 capsules</span></div>
  </article>

  <article class="pack" style="--top:#cc1238;--strip:#f7dca0">
    <div class="pack__band"></div><div class="pack__strip"></div>
    <div class="pack__shell" role="img" aria-label="Liposomal shell ring graphic"></div>
    <h2 class="pack__title">M368 FORTIVAN</h2>
    <p class="pack__subtitle">Collagen optimizer</p>
    <p class="pack__process">Processed with liposomal nanotechnology</p>
    <p class="pack__note">Dietary supplement product</p>
    <div class="pack__footer"><span>Genuine product of Thailand</span><span>30 capsules</span></div>
  </article>

  <article class="pack pack--light" style="--top:#f9e01a;--strip:#dccfe6">
    <div class="pack__band"></div><div class="pack__strip"></div>
    <div class="pack__shell" role="img" aria-label="Liposomal shell ring graphic"></div>
    <h2 class="pack__title">L975 CELLORA</h2>
    <p class="pack__subtitle">Cells turnover enhancer</p>
    <p class="pack__process">Processed with liposomal nanotechnology</p>
    <p class="pack__note">Dietary supplement product</p>
    <div class="pack__footer"><span>Genuine product of Thailand</span><span>30 capsules</span></div>
  </article>

  <article class="pack" style="--top:#a0248a;--strip:#dcc9e6">
    <div class="pack__band"></div><div class="pack__strip"></div>
    <div class="pack__shell" role="img" aria-label="Liposomal shell ring graphic"></div>
    <h2 class="pack__title">E651 OXIGUARD</h2>
    <p class="pack__subtitle">Antioxidants complex</p>
    <p class="pack__process">Processed with liposomal nanotechnology</p>
    <p class="pack__note">Dietary supplement product</p>
    <div class="pack__footer"><span>Genuine product of Thailand</span><span>30 capsules</span></div>
  </article>

  <article class="pack" style="--top:#e01020;--strip:#f4cad0">
    <div class="pack__band"></div><div class="pack__strip"></div>
    <div class="pack__shell" role="img" aria-label="Liposomal shell ring graphic"></div>
    <h2 class="pack__title">L548 CALMOFLEX</h2>
    <p class="pack__subtitle">Anti-inflammatory complex</p>
    <p class="pack__process">Processed with liposomal nanotechnology</p>
    <p class="pack__note">Dietary supplement product</p>
    <div class="pack__footer"><span>Genuine product of Thailand</span><span>30 capsules</span></div>
  </article>

  <article class="pack" style="--top:#ec6e12;--strip:#f6eea0">
    <div class="pack__band"></div><div class="pack__strip"></div>
    <div class="pack__shell" role="img" aria-label="Liposomal shell ring graphic"></div>
    <h2 class="pack__title">L583 SOLARIX</h2>
    <p class="pack__subtitle">Oral sunscreen complex</p>
    <p class="pack__process">Processed with liposomal nanotechnology</p>
    <p class="pack__note">Dietary supplement product</p>
    <div class="pack__footer"><span>Genuine product of Thailand</span><span>30 capsules</span></div>
  </article>

</main>
</body>
</html>
```